Vectrix Optimal Web Design Project

Web design for a company that highlights the people and experience behind a company that develops solutions, both through the provision of professional services, as well as software development, using mathematical optimisation tools. We want it to be professional looking (minimal bright flashy colors and animation) and allow us to easily update it after delivery without having to purchase any 3rd party software tools. Minimum tabs: About us, services, products, careers, contact. Search box to search site content, including ad-hoc documents add to site (PDF).
The design should emphasis simplicity and professionalism. We need to be able to link documents to the site easily as we add research papers, project descriptions, key personnel resume's etc etc.
Target Market(s)
Technical professionals, researchers, academics
Industry/Entity Type
Software
Look and feel

```html
<!DOCTYPE html>
<html lang="en">
<head>
<meta charset="utf-8">
<title>Vectrix Optimal — Software Development</title>
<link href="https://fonts.googleapis.com/css2?family=Open+Sans:wght@300;400;600;700&display=swap" rel="stylesheet">
<style>
:root{
  --orange:#f47a12;
  --orange-dark:#d95f00;
  --green:#2fa51f;
  --green-dark:#1d8612;
  --blue:#1e9be0;
  --text:#333;
  --muted:#777;
  --light:#999;
  --line:#e2e2e2;
  --page:#fafafa;
  --band:#e6e6e6;
  --footer:#f1f1f1;
}
*{box-sizing:border-box;margin:0;padding:0}
html,body{width:852px;height:1200px;overflow:hidden}
body{position:relative;background:var(--page);font-family:"Open Sans",Arial,sans-serif;color:var(--text)}
.abs{position:absolute}

/* header */
.brand{left:97px;top:28px;display:flex;align-items:center;gap:8px}
.brand-dot{width:26px;height:26px;border-radius:50%;background:var(--orange)}
.brand-name{font-size:17px;font-weight:700;color:#222;line-height:1}
.phone{left:582px;top:18px;display:flex;align-items:center;gap:10px}
.phone-tag{background:var(--blue);color:#fff;font-weight:600;font-size:14px;padding:5px 20px 5px 12px;clip-path:polygon(0 0,90% 0,100% 50%,90% 100%,0 100%)}
.nav{left:218px;top:59px;width:540px;display:flex;align-items:center;border-bottom:1px solid var(--line);height:28px}
.nav a{font-size:12.5px;color:#444;text-decoration:none;padding:2px 11px;margin-right:4px}
.nav a.active{background:var(--orange);color:#fff;border-radius:2px}
.search{left:596px;top:58px;width:162px;height:22px;border:1px solid #ddd;background:#fff;display:flex;align-items:center;padding-left:8px;font-size:8px;color:#aaa}
.search-go{position:absolute;right:-1px;top:-1px;width:26px;height:22px;background:var(--green);color:#fff;font-size:8px;font-weight:700;display:flex;align-items:center;justify-content:center;clip-path:polygon(20% 0,100% 0,100% 100%,20% 100%,0 50%)}

/* hero */
.hero-title{left:94px;top:134px;font-size:29px;font-weight:400;color:#222;letter-spacing:-.3px;white-space:nowrap}
.hero-sub{left:94px;top:169px;width:300px;font-size:14px;line-height:16px;color:#333}
.hero-copy{left:94px;top:205px;width:300px;font-size:9.5px;line-height:13.5px;color:#777}
.btn{display:flex;align-items:center;justify-content:center;gap:8px;color:#fff;font-size:13px;border-radius:2px;white-space:nowrap}
.btn-orange{background:linear-gradient(#fb8d2c,var(--orange-dark))}
.btn-green{background:linear-gradient(#3dbb2a,var(--green-dark))}
.hero-btn1{left:94px;top:280px;width:142px;height:32px}
.hero-btn2{left:245px;top:280px;width:141px;height:32px}
.ico{width:11px;height:11px;border:1.5px solid #fff;border-radius:1px}
.hero-media{left:428px;top:128px;width:332px;height:212px;border-radius:6px;background:linear-gradient(135deg,#3b3b3b,#7d8a98 55%,#d9c7a3)}

/* tabs */
.tabband{left:0;top:358px;width:852px;height:40px;background:linear-gradient(#f1f1f1,#dcdcdc);border-top:1px solid #d5d5d5;border-bottom:1px solid #cfcfcf}
.tab{top:362px;height:36px;display:flex;align-items:center;justify-content:center;gap:8px;font-size:12px;color:#555;border-left:1px solid #d0d0d0}
.tab.active{background:#fff;color:var(--blue);border:1px solid #d0d0d0;border-bottom:none;height:37px}
.tab svg{width:12px;height:12px}

/* projects */
.proj-art{left:108px;top:440px;width:176px;height:150px;border-radius:4px;background:linear-gradient(160deg,#cfe8fb,#3d9be0 60%,#e3e3e3)}
.proj-title{left:326px;top:430px;font-size:14px;font-weight:700;color:var(--orange);white-space:nowrap}
.proj-copy{left:326px;top:451px;width:400px;font-size:8.5px;line-height:13px;color:#777}
.proj-thumb{top:505px;width:83px;height:83px;border-radius:50%;border:3px solid #fff;box-shadow:0 1px 4px rgba(0,0,0,.25)}
.proj-link{left:0;top:607px;width:852px;text-align:center;font-size:8.5px;color:#666}
.proj-link b{color:var(--green);font-weight:600}

/* team */
.team{left:92px;top:643px;width:670px;height:320px;border:1px solid #e0e0e0;background:#f6f6f6;border-radius:3px}
.team-title{left:122px;top:656px;font-size:15px;font-weight:600;color:var(--blue)}
.team-all{left:613px;top:643px;width:129px;height:37px;font-size:12.5px}
.member{top:706px;width:150px;text-align:center}
.member-photo{width:114px;height:114px;border-radius:50%;margin:0 auto;border:3px solid #fff;box-shadow:0 1px 5px rgba(0,0,0,.2);background:linear-gradient(160deg,#d9d1c6,#8a7f74)}
.member-name{margin-top:24px;font-size:11px;color:var(--orange);white-space:nowrap}
.member-role{font-size:10.5px;color:#999;line-height:14px;white-space:nowrap}
.member-bio{font-size:8.5px;line-height:12.5px;color:#666;margin-top:2px;padding:0 8px}
.more{display:inline-block;margin-top:6px;background:#666;color:#eee;font-size:7px;padding:2px 7px;border-radius:2px}

/* cta */
.cta1{left:187px;top:990px;width:201px;height:32px;font-size:14px}
.cta-and{left:414px;top:996px;font-size:16px;font-style:italic;color:#999;font-family:Georgia,serif}
.cta2{left:471px;top:990px;width:201px;height:32px;font-size:14px}

/* footer */
.footer{left:0;top:1046px;width:852px;height:154px;background:var(--footer);border-top:1px solid #e4e4e4}
.fcol{top:1068px}
.fcol h4{font-size:9.5px;font-weight:400;color:var(--blue);margin-bottom:3px}
.fcol li{list-style:none;font-size:8px;line-height:14px;color:#666;white-space:nowrap}
.fcol li::before{content:"» ";color:#999}
.fcol li.hl{color:var(--orange)}
.social li::before{content:""}
.social li{display:flex;align-items:center;gap:6px;line-height:15px}
.sq{width:9px;height:9px;border-radius:1px}
.flogo{left:645px;top:1120px;display:flex;align-items:center;gap:6px}
.flogo span:first-child{width:20px;height:20px;border-radius:50%;background:#ccc}
.flogo span:last-child{font-size:14px;font-weight:700;color:#aaa}
.copy{left:0;top:1184px;width:852px;text-align:center;font-size:8px;color:#888}
</style>
</head>
<body>

<header>
  <div class="abs brand"><span class="brand-dot"></span><span class="brand-name">Vectrix Optimal</span></div>
  <div class="abs phone">
    <svg width="18" height="16" viewBox="0 0 18 16"><path d="M2 5c0-3 14-3 14 0v2h-4V5H6v2H2z" fill="#777"/><rect x="4" y="8" width="10" height="7" rx="1" fill="#777"/></svg>
    <span class="phone-tag">Tel. 01XXX 318 506</span>
  </div>
  <nav class="abs nav">
    <a href="#">About Us</a><a href="#">Services</a><a href="#" class="active">Products</a><a href="#">Careers</a><a href="#">Contact</a>
  </nav>
  <div class="abs search">Search...<span class="search-go">Go</span></div>
</header>

<section class="hero">
  <h1 class="abs hero-title">Software Development</h1>
  <p class="abs hero-sub">Give your business an Edge with picture perfect solutions.</p>
  <p class="abs hero-copy">It is a long established fact that a reader will be distracted by the readable content of a page when looking at its layout. The point of using Lorem Ipsum is that it has a more-or-less normal distribution of letters, as opposed to using 'Content...</p>
  <a class="abs btn btn-orange hero-btn1"><span class="ico"></span>Request Services</a>
  <a class="abs btn btn-green hero-btn2"><span class="ico"></span>Get Easy Solutions</a>
  <div class="abs hero-media" role="img" aria-label="Website shown on desktop monitor, tablet and phone"></div>
</section>

<div class="abs tabband"></div>
<div class="abs tab" style="left:92px;width:183px"><svg viewBox="0 0 12 12"><rect x="1" y="4" width="10" height="7" fill="#555"/><rect x="4" y="2" width="4" height="3" fill="none" stroke="#555"/></svg>Our Experience</div>
<div class="abs tab" style="left:275px;width:166px"><svg viewBox="0 0 12 12"><circle cx="4" cy="4" r="2" fill="#555"/><circle cx="8.5" cy="4.5" r="1.7" fill="#555"/><path d="M0 11c0-4 8-4 8 0zM7 11c0-3 5-3 5 0z" fill="#555"/></svg>Peoples</div>
<div class="abs tab active" style="left:441px;width:164px"><svg viewBox="0 0 12 12"><path d="M6 0l1.8 4 4.2.4-3.2 2.8 1 4.3L6 9.2 2.2 11.5l1-4.3L0 4.4 4.2 4z" fill="#1e9be0"/></svg>Our Projects</div>
<div class="abs tab" style="left:605px;width:152px;border-right:1px solid #d0d0d0"><svg viewBox="0 0 12 12"><circle cx="6" cy="4.5" r="3.5" fill="#555"/><rect x="4.5" y="8" width="3" height="3" fill="#555"/></svg>Solutions</div>

<section class="projects">
  <div class="abs proj-art" role="img" aria-label="Blueprint plans with drafting tools"></div>
  <h2 class="abs proj-title">Projects Lorem Ipsum is simply dummy text of the printing...</h2>
  <p class="abs proj-copy">It is a long established fact that a reader will be distracted by the readable content of a page when looking at its layout. The point of using Lorem Ipsum is that it has a more-or-less normal distribution of letters, as opposed to using 'Content here, content here', making it look like readable English.</p>
  <div class="abs proj-thumb" style="left:328px;background:linear-gradient(135deg,#3aa0e0,#f1f1f1)" role="img" aria-label="Project screenshot: business website"></div>
  <div class="abs proj-thumb" style="left:438px;background:linear-gradient(135deg,#f3f3f3,#d83a3a)" role="img" aria-label="Project screenshot: web hosting site"></div>
  <div class="abs proj-thumb" style="left:540px;background:linear-gradient(135deg,#fafafa,#cfd8c8)" role="img" aria-label="Project screenshot: diagram application"></div>
  <div class="abs proj-thumb" style="left:652px;background:linear-gradient(135deg,#6a4a3a,#d94f6a)" role="img" aria-label="Project screenshot: fashion shop"></div>
  <p class="abs proj-link"><b>Click here</b> to read what people are saying about Vectrix Optimal, or <b>check out our recent work »</b></p>
</section>

<section class="abs team"></section>
<h2 class="abs team-title">Our Team</h2>
<a class="abs btn btn-orange team-all"><span class="ico" style="border-radius:50%"></span>View All Team</a>

<div class="abs member" style="left:99px">
  <div class="member-photo" role="img" aria-label="Portrait of team member"></div>
  <div class="member-name">Helen Mardle</div><div class="member-role">Software developer</div>
  <p class="member-bio">It is a long established fact that a reader will be distracted by the readable content of a page when looking at its layout....</p><span class="more">read more</span>
</div>
<div class="abs member" style="left:271px">
  <div class="member-photo" role="img" aria-label="Portrait of team member"></div>
  <div class="member-name">Tom Ashby</div><div class="member-role">Designer</div>
  <p class="member-bio">It is a long established fact that a reader will be distracted by the readable content of a page when looking at its layout....</p><span class="more">read more</span>
</div>
<div class="abs member" style="left:436px">
  <div class="member-photo" role="img" aria-label="Portrait of team member"></div>
  <div class="member-name">Anna Corbett</div><div class="member-role">Projects Director</div>
  <p class="member-bio">It is a long established fact that a reader will be distracted by the readable content of a page when looking at its layout....</p><span class="more">read more</span>
</div>
<div class="abs member" style="left:602px">
  <div class="member-photo" role="img" aria-label="Portrait of team member"></div>
  <div class="member-name">Peter Hollis</div><div class="member-role">Development Manager</div>
  <p class="member-bio">It is a long established fact that a reader will be distracted by the readable content of a page when looking at its layout....</p><span class="more">read more</span>
</div>

<a class="abs btn btn-orange cta1"><span class="ico"></span>Request Services</a>
<span class="abs cta-and">and</span>
<a class="abs btn btn-green cta2"><span class="ico"></span>Get Easy Solutions</a>

<footer class="abs footer"></footer>
<div class="abs fcol" style="left:95px"><h4>About Us</h4><ul><li>Overview</li><li>Values &amp; Culture</li><li>Our Clients</li><li>Testimonials</li><li>Our Team</li><li>Latest News</li></ul></div>
<div class="abs fcol" style="left:208px"><h4>Service Offerings</h4><ul><li>Website Design</li><li>Web Design</li><li>Web Application Development</li><li class="hl">Mobile Application Development</li><li>Software QA &amp; Testing</li></ul></div>
<div class="abs fcol" style="left:373px"><h4>Knowledge Center</h4><ul><li>Technology Expertise</li><li>Blog</li><li>Latest Articles</li><li>FAQ's</li><li>Newsletters</li></ul></div>
<div class="abs fcol social" style="left:502px"><h4>Follow Us</h4><ul>
  <li><span class="sq" style="background:#bbb"></span>Subscribe to Blog</li>
  <li><span class="sq" style="background:#5bbcec"></span>Follow us on Chirpline</li>
  <li><span class="sq" style="background:#4a6aa8"></span>Be a fan on Friendbook</li>
  <li><span class="sq" style="background:#f59a2a"></span>RSS Feed</li></ul></div>
<div class="abs flogo"><span></span><span>Vectrix Optimal</span></div>
<p class="abs copy">© 2013 Vectrix Optimal all rights reserved</p>

</body>
</html>
```